Business card and stationary for eco-aware technology company
Verdalux: Green-minded Scrap Recovery
Business card and stationary for eco-aware technology company - Chemicals
Creative Brief
Professional
Tam Brendow
Managing Director
7-3, 2nd Floor, Pelham Court, Quarry Road, 10450 Georgetown, Penang, Malaysia
+604-8XXXXXX
+6011-5274 XXXX
xxx@verdalux.example
http://www.verdalux.example
YYYYYYY-K
Hello, My name is Tam Brendow, and I am MD of Verdalux. I would like a letterhead and a business card for myself. Verdalux is a Malaysia-based startup with a focus on developing technology for urban mining ( http://scrapharvest.example/ ). Verdalux's name is legally Verdalux Sdn. Bhd., but maybe the shorter form, 'Verdalux' looks better on a business card. Perhaps the "Sdn. Bhd." could be hidden in there somewhere. Up to you! For the business card, the following info should be used: Tam Brendow Managing Director MChem, Ph.D (Chemistry) The back side of the business card can be blank, or it can be very simply decorated. I am on Malaysian time (GMT +8) so please forgive me if my feedback appears delayed. Thanks & good luck, - Tam
Empty is fine. Very simple decoration if you want - maybe just the company logo in the center.
tbrendow tbrendow
Hey, Sorry for the slow feedback. I've just got back to the office. Firstly, I am happy to review the business card designs on this site. However, the stationary designs are too big to preview and quorbasketch's site makes it too slow for me to look at the designs. So, would you designers be able to host the images on a web server, or put them in a .zip file? Private message me the URL and I'll download them and use an image viewer to see them offline. Sorry for the extra work - blame QS's crap design. Ok, now for some feedback: 1) The dark 'Eco' green does not look nice on the card. Please use only a little bit! 2) Lighter greens are nice. Like the colour of the 3 leaves. 3) No transparent cards, please. 4) The back of the card should have a very simple design. Maybe just the 3 leaves on a white background, with no text? 5) I love the designs with the big leaf (#191). It's clever. I also love the designs with the circuit pattern (#212, #213, #214). That's clever too. Private message me if you want more feedback or ideas. I'll try to reply fast. Thanks, - Tam

```html
<!DOCTYPE html>
<html lang="en">
<head>
<meta charset="utf-8">
<title>Verdalux Business Card</title>
<link href="https://fonts.googleapis.com/css2?family=Open+Sans:wght@400;600;700;800&display=swap" rel="stylesheet">
<style>
  :root {
    --bg: #e4e6e3;
    --green-deep: #1f6a2c;
    --green-mid: #2f8a3a;
    --green-light: #8cc63f;
    --ink: #3c3c3c;
    --muted: #6a6a6a;
    --white: #ffffff;
  }
  * { box-sizing: border-box; margin: 0; padding: 0; }
  html, body { width: 1200px; height: 751px; overflow: hidden; }
  body {
    background: var(--bg);
    font-family: "Open Sans", Arial, sans-serif;
    color: var(--ink);
    position: relative;
  }
  .card {
    position: absolute;
    top: 227px;
    width: 520px;
    height: 297px;
    border-radius: 14px;
    overflow: hidden;
    box-shadow: 0 6px 18px rgba(0,0,0,.18);
  }
  /* Back side */
  .card-back { left: 60px; background: var(--green-mid); }
  .back-texture {
    position: absolute; inset: 0;
    background: radial-gradient(ellipse at 50% 45%, #3a9a45 0%, var(--green-mid) 45%, var(--green-deep) 100%);
  }
  .back-brand {
    position: absolute; left: 0; right: 0; top: 100px;
    display: flex; align-items: center; justify-content: center; gap: 12px;
  }
  .back-brand .mark-dot {
    width: 34px; height: 34px; border-radius: 50%; background: var(--green-light);
  }
  .back-brand .brand-name {
    font-weight: 700; font-size: 32px; color: var(--green-light); letter-spacing: .5px;
  }
  .back-web {
    position: absolute; left: 0; right: 0; top: 186px;
    text-align: center; font-size: 10px; letter-spacing: 2px; color: rgba(255,255,255,.8);
  }
  .back-rule {
    position: absolute; left: 150px; right: 150px; top: 204px; height: 1px;
    background: rgba(255,255,255,.35);
  }
  /* Front side */
  .card-front { left: 620px; background: var(--white); }
  .edge-tab { position: absolute; background: var(--green-mid); }
  .edge-tab.right { right: 0; top: 118px; width: 9px; height: 72px; border-radius: 4px 0 0 4px; }
  .edge-tab.left { left: 0; top: 238px; width: 9px; height: 40px; border-radius: 0 4px 4px 0; }
  .logo {
    position: absolute; left: 30px; top: 50px;
    display: flex; align-items: center; gap: 10px;
  }
  .logo .mark-dot { width: 38px; height: 38px; border-radius: 50%; background: var(--green-light); }
  .logo .brand-name { font-weight: 700; font-size: 34px; color: var(--green-mid); line-height: 1; }
  .tagline {
    position: absolute; left: 80px; top: 90px;
    font-size: 7.5px; font-weight: 600; letter-spacing: 1.3px; color: var(--green-mid);
  }
  .person {
    position: absolute; right: 34px; top: 110px; text-align: right;
  }
  .person .name { font-size: 15px; font-weight: 700; color: var(--green-mid); }
  .person .cred, .person .role { font-size: 9px; color: var(--muted); line-height: 1.5; }
  .details {
    position: absolute; left: 30px; top: 130px; font-size: 8.5px; color: var(--muted); line-height: 1.45;
  }
  .details .address { margin-bottom: 6px; width: 170px; }
  .contact-list { list-style: none; }
  .contact-list li { display: flex; align-items: center; gap: 7px; height: 15px; }
  .contact-list svg { width: 10px; height: 10px; fill: var(--green-mid); flex: none; }
</style>
</head>
<body>

<section class="card card-back" aria-label="Business card back">
  <div class="back-texture" role="img" aria-label="Soft green background with faint leaf pattern"></div>
  <div class="back-brand">
    <span class="mark-dot"></span>
    <span class="brand-name">Verdalux</span>
  </div>
  <p class="back-web">www.verdalux.example</p>
  <div class="back-rule"></div>
</section>

<section class="card card-front" aria-label="Business card front">
  <div class="edge-tab right"></div>
  <div class="edge-tab left"></div>

  <div class="logo">
    <span class="mark-dot"></span>
    <span class="brand-name">Verdalux</span>
  </div>
  <p class="tagline">GREEN-MINDED SCRAP RECOVERY</p>

  <div class="person">
    <p class="name">Tam Brendow</p>
    <p class="cred">MChem, Ph.D (Chemistry)</p>
    <p class="role">Managing Director</p>
  </div>

  <div class="details">
    <p class="address">License No: YYYYYYY-K<br>
      7-3, 2nd Floor, Pelham Court,<br>
      Quarry Road, 10450 Georgetown,<br>
      Penang, Malaysia</p>
    <ul class="contact-list">
      <li><svg viewBox="0 0 24 24"><path d="M6.6 10.8a15 15 0 0 0 6.6 6.6l2.2-2.2a1 1 0 0 1 1-.25 11.4 11.4 0 0 0 3.6.57 1 1 0 0 1 1 1V20a1 1 0 0 1-1 1A17 17 0 0 1 3 4a1 1 0 0 1 1-1h3.5a1 1 0 0 1 1 1c0 1.25.2 2.45.57 3.6a1 1 0 0 1-.25 1z"/></svg>+604-8XXXXXX</li>
      <li><svg viewBox="0 0 24 24"><path d="M7 1h10a2 2 0 0 1 2 2v18a2 2 0 0 1-2 2H7a2 2 0 0 1-2-2V3a2 2 0 0 1 2-2zm0 3v14h10V4zm5 15.5a1.2 1.2 0 1 0 0 2.4 1.2 1.2 0 0 0 0-2.4z"/></svg>+6011-5274 XXXX</li>
      <li><svg viewBox="0 0 24 24"><path d="M2 5h20v14H2zm2 2v.5l8 5 8-5V7zm0 2.9V17h16V9.9l-8 5z"/></svg>xxx@verdalux.example</li>
      <li><svg viewBox="0 0 24 24"><path d="M12 2a10 10 0 1 0 0 20 10 10 0 0 0 0-20zm6.9 9h-3a15 15 0 0 0-1.3-5.6A8 8 0 0 1 18.9 11zM12 4.1c.9 1.2 1.8 3.6 1.9 6.9h-3.8c.1-3.3 1-5.7 1.9-6.9zM9.4 5.4A15 15 0 0 0 8.1 11h-3a8 8 0 0 1 4.3-5.6zM5.1 13h3a15 15 0 0 0 1.3 5.6A8 8 0 0 1 5.1 13zm6.9 6.9c-.9-1.2-1.8-3.6-1.9-6.9h3.8c-.1 3.3-1 5.7-1.9 6.9zm2.6-1.3a15 15 0 0 0 1.3-5.6h3a8 8 0 0 1-4.3 5.6z"/></svg>http://www.verdalux.example</li>
    </ul>
  </div>
</section>

</body>
</html>
```